Need a image for a Chirpline ad campaign

Need a image designed for a Chirpline ad campaign. We are setting up a Chirpline campaign advertising on Chirpline for people who would want to get into modelling. We accept people aged 4+ . We want them to go to stepuptoposing dot com to sign up and apply. We need this image to comply with Chirpline ad policies. It can't have more than 20% text on it.

Maybe just say Become a Model or something
Step Up to Posing or something your choice.

What size should my ad image be?

The best image size to use for your ad depends on what type of ad you're creating, but a best practice is to size your images to be 1200 x 628 pixels. The Promo Format Manual contains all of the specifications around the recommended ad image sizes for each ad type. If your image is larger or smaller than the dimensions specified in the Promo Format Manual, it will be automatically resized to fit in the ad. Animated or flash images aren't supported.

Keep in mind that your ad may not contain more than 20% text in the ad's image.

Target Market(s)

People who would want to get into modelling

Industry/Entity Type

Advertising

Font styles to use
Sans Serif

Colors

Designer to choose colors to be used in the design.

Requirements
Must have
• Must tie in with the main website stepuptoposing dot com

```html
<!DOCTYPE html>
<html lang="en">
<head>
<meta charset="utf-8">
<title>Step Up to Posing – Become a Model</title>
<link rel="stylesheet" href="https://fonts.googleapis.com/css2?family=Roboto+Condensed:wght@700&display=swap">
<style>
  :root {
    --bg-deep: #1c1c1c;
    --bg-mid: #3a3836;
    --lens-glow: #5a2418;
    --headline: #ddaa0c;
    --subline: #ffffff;
    --button-fill: #6c5e49;
    --button-text: #1e1a12;
    --button-edge: #c8a04a;
  }
  * { box-sizing: border-box; margin: 0; padding: 0; }
  html, body {
    width: 1200px;
    height: 628px;
    overflow: hidden;
    background: var(--bg-deep);
  }
  .ad {
    position: relative;
    width: 1200px;
    height: 628px;
    overflow: hidden;
    font-family: "Roboto Condensed", "Arial Narrow", sans-serif;
    font-weight: 700;
    text-transform: uppercase;
  }
  .ad__photo {
    position: absolute;
    inset: 0;
    background:
      radial-gradient(circle at 680px 330px, var(--lens-glow) 0, rgba(40,20,16,0.9) 60px, rgba(20,18,16,0) 170px),
      radial-gradient(ellipse 420px 300px at 900px 250px, rgba(150,140,128,0.45), rgba(0,0,0,0) 100%),
      radial-gradient(ellipse 500px 260px at 420px 560px, rgba(110,104,96,0.5), rgba(0,0,0,0) 100%),
      radial-gradient(ellipse 600px 300px at 300px 120px, rgba(90,88,84,0.45), rgba(0,0,0,0) 100%),
      linear-gradient(160deg, var(--bg-mid) 0%, var(--bg-deep) 55%, #2a2826 100%);
  }
  .ad__headline {
    position: absolute;
    top: 152px;
    left: 8px;
    width: 100%;
    text-align: center;
    color: var(--headline);
    font-size: 68px;
    line-height: 1;
    letter-spacing: 0.5px;
    white-space: nowrap;
    text-shadow: 0 2px 4px rgba(0,0,0,0.5);
  }
  .ad__subline {
    position: absolute;
    top: 292px;
    left: 18px;
    width: 100%;
    text-align: center;
    color: var(--subline);
    font-size: 28px;
    line-height: 1;
    letter-spacing: 0.5px;
    white-space: nowrap;
  }
  .cta {
    position: absolute;
    left: 395px;
    top: 403px;
    width: 435px;
    height: 62px;
  }
  .cta__shape { position: absolute; inset: 0; }
  .cta__label {
    position: absolute;
    inset: 0;
    display: flex;
    align-items: center;
    justify-content: center;
    color: var(--button-text);
    font-size: 32px;
    letter-spacing: 0.5px;
    white-space: nowrap;
    text-shadow: 1px 1px 0 var(--button-edge);
  }
</style>
</head>
<body>
  <main class="ad">
    <div class="ad__photo" role="img" aria-label="Dark, softly blurred photograph of a hand holding a vintage film camera with a red-tinted lens"></div>
    <h1 class="ad__headline">Do you want to become a model?</h1>
    <p class="ad__subline">Apply now at stepuptoposing dot com</p>
    <div class="cta">
      <svg class="cta__shape" width="435" height="62" viewBox="0 0 435 62" aria-hidden="true">
        <polygon points="0,31 34,0 401,0 435,31 401,62 34,62" fill="var(--button-fill)"/>
      </svg>
      <span class="cta__label">Register yourself</span>
    </div>
  </main>
</body>
</html>
```